Lantern - Web Design Project

We are seeking to have our website redesigned. Our current webpage is rather dated looking www.lantern-outcomes.com We will be utilizing similar content to explain our services as what is in the website now. We do not see it at a retail portal but rather a website for those inquiring about our services as a reference check so to speak.

We wish to have a look that is considered clean, fresh, contemporary and contains a business savvy vibe.

We prefer isolated white background and also wish to retain the integrity of our Logo and colour scheme.

We are looking for something that doesnt look like it was designed at home on sitemoose. We are hoping to find something that looks like it would reside on a tablet.
Updates

Hello designers!

We apologize for our tardiness as we have been quite preoccupied. We will be extending our invites to the end of January!

Hello All,

Please review our offer once again for updated requirements.  We are hoping to accept a design by months end.

Lantern

Target Market(s)

Business to business clients and Large manufacturers

Industry/Entity Type

Retail

Requirements
Must have
• Existing Logo

There must be an area dedicated to an intro video that will be incorporated on our landing page.

We require design of the other pages as well not only the landing page.

```html
<!DOCTYPE html>
<html lang="en">
<head>
<meta charset="utf-8">
<title>Lantern Performance Group</title>
<link href="https://fonts.googleapis.com/css2?family=Oswald:wght@400;500;600&family=PT+Sans:wght@400;700&family=PT+Sans+Narrow:wght@400;700&display=swap" rel="stylesheet">
<style>
:root{
  --page:#e6e6e6;
  --header:#e9e9e9;
  --red:#d8161b;
  --red-dark:#a80d10;
  --navy:#0f2c5c;
  --nav-bar:#7a7a7a;
  --search-band:#5a5352;
  --input:#8c8c8c;
  --text:#555;
  --ink:#222;
  --white:#fff;
}
*{margin:0;padding:0;box-sizing:border-box}
html,body{width:1200px;height:1134px;overflow:hidden}
body{position:relative;background:var(--page);font-family:Arial,Helvetica,sans-serif;color:var(--text)}
.abs{position:absolute}

.site-header{left:0;top:12px;width:1200px;height:150px;background:linear-gradient(#ececec,#e2e2e2);box-shadow:0 3px 6px rgba(0,0,0,.15)}
.brand{left:54px;top:52px;display:flex;align-items:center;gap:12px;font-family:"PT Sans",sans-serif;font-weight:700;font-size:58px;color:#4a4646;line-height:1}
.brand-dot{width:20px;height:20px;border-radius:50%;background:var(--red)}

.top-tab{top:6px;height:36px;background:linear-gradient(#e52a2a,#c50f12);color:var(--white);font-family:"Oswald",sans-serif;font-size:21px;text-align:center;line-height:36px;border-top:4px solid #222;box-shadow:0 2px 3px rgba(0,0,0,.3)}
.tab-signin{left:860px;width:108px}
.tab-language{left:1016px;width:133px}

.nav-panel{left:341px;top:54px;width:826px;height:90px;background:#ebebeb;box-shadow:-6px 0 10px rgba(0,0,0,.12)}
.main-nav{left:348px;top:80px;width:819px;height:45px;background:linear-gradient(#8a8a8a,#6e6e6e);display:flex;align-items:center;padding-left:13px;gap:0}
.main-nav a{font-family:"PT Sans Narrow",sans-serif;font-size:19px;color:var(--white);text-decoration:none;padding:0 11px;line-height:40px;text-shadow:0 1px 1px rgba(0,0,0,.5)}
.main-nav a.active{background:var(--red);color:#111;text-shadow:none;padding:0 10px}

.hero{left:0;top:166px;width:1200px;height:314px}
.hero-photo{position:absolute;inset:0;background:linear-gradient(100deg,#f4f4f4 0%,#d9dcdf 28%,#8e9398 45%,#6f757a 60%,#c6c9cc 80%,#f2f2f2 100%)}
.hero-title{left:58px;top:210px;font-family:"Oswald",sans-serif;font-weight:600;font-size:56px;color:#5d5a5a;letter-spacing:1px;text-shadow:2px 2px 2px rgba(0,0,0,.35)}
.hero-line{font-family:"PT Sans Narrow",sans-serif;font-size:26px;color:#111;text-shadow:0 1px 1px rgba(255,255,255,.6)}
.hero-line b{font-weight:400;font-size:38px;color:var(--white);text-shadow:1px 1px 2px rgba(0,0,0,.4)}
.hero-line-1{left:136px;top:296px}
.hero-line-2{left:146px;top:344px}
.btn-red{background:linear-gradient(#ee2b2b,#c30d10);color:var(--white);font-family:"Oswald",sans-serif;border-radius:4px;box-shadow:0 3px 5px rgba(0,0,0,.4);display:flex;align-items:center;justify-content:center;gap:10px}
.hero-signup{left:323px;top:396px;width:198px;height:54px;font-size:23px}
.hero-dots{left:64px;top:450px;display:flex;gap:12px}
.hero-dots span{width:12px;height:12px;border-radius:50%;background:#777}
.hero-dots span.on{background:#7dc242}

.search-band{left:17px;top:502px;width:1166px;height:56px;background:var(--search-band);box-shadow:0 4px 8px rgba(0,0,0,.25)}
.search-input{left:54px;top:513px;width:1036px;height:37px;background:var(--input);border:2px solid #a8a8a8;color:#f2f2f2;font-size:16px;line-height:33px;padding-left:12px}
.search-go{left:1100px;top:512px;width:48px;height:38px;background:var(--red);color:var(--white);font-family:"Oswald",sans-serif;font-size:25px;text-align:center;line-height:38px}

.welcome{left:56px;top:574px;font-family:"PT Sans",sans-serif;color:var(--red);font-size:40px;white-space:nowrap}
.welcome small{font-family:"PT Sans Narrow",sans-serif;font-size:30px;color:var(--navy);font-weight:400}

.intro-slider{left:53px;top:637px;width:1095px;height:92px;background:var(--white);border:1px solid #ccc;box-shadow:0 6px 8px -6px rgba(0,0,0,.3)}
.intro-slider h3{position:absolute;left:51px;top:14px;font-size:15px;font-weight:400;color:#111}
.intro-slider p{position:absolute;left:48px;font-size:14px;color:#333}
.intro-slider .p1{top:37px}.intro-slider .p2{top:59px}
.slide-arrow{position:absolute;top:34px}

.col-heading{top:770px;height:26px;display:flex;align-items:center;font-family:"PT Sans",sans-serif;font-size:22px;color:var(--navy)}
.col-heading::before,.col-heading::after{content:"";flex:1;height:8px;background:var(--white)}
.col-heading span{padding:0 10px}
.col-1{left:53px;width:340px}.col-2{left:429px;width:340px}.col-3{left:807px;width:340px}

.video-frame{left:53px;top:806px;width:340px;height:184px;border:3px solid #bdbdbd;background:#aaa}
.video-still{position:absolute;left:3px;top:3px;width:328px;height:136px;background:linear-gradient(90deg,#8e8a86,#c9b9b2 45%,#d9d2cc 70%,#e6e2de)}
.video-controls{position:absolute;left:3px;top:139px;width:328px;height:36px;background:#000}

.news-box{left:429px;top:806px;width:340px;height:184px;background:#f8f8f8;border:3px solid #dcdcdc}
.news-item{position:absolute;left:34px;width:290px;font-size:14.4px;line-height:19px;color:#8a8a8a;text-align:justify}
.news-item::before{content:"»";position:absolute;left:-24px;top:-2px;font-size:20px;color:#aaa}
.news-1{top:14px}.news-2{top:90px}

.promo-box{left:807px;top:806px;width:340px;height:184px;border:1px solid #ccc;overflow:hidden}
.promo-photo{position:absolute;inset:0;background:linear-gradient(120deg,#6a5a52,#a68a78 40%,#e8e4df 55%,#4e4f58 80%,#2e3038)}
.promo-title{position:absolute;left:20px;top:28px;font-family:"Oswald",sans-serif;font-size:21px;color:var(--white);text-shadow:1px 1px 2px rgba(0,0,0,.6)}
.promo-signup{position:absolute;left:162px;top:98px;width:158px;height:50px;font-size:22px;border:2px solid #f06060}

.site-footer{left:0;top:1039px;width:1200px;height:95px;background:linear-gradient(#e2e2e2,#dadada);border-top:3px solid #cfcfcf}
.footer-nav{left:0;top:1061px;width:1200px;display:flex;justify-content:center;gap:24px;padding-right:50px;font-size:14.4px}
.footer-nav a{color:#666;text-decoration:none}
.footer-nav a.active{color:#000}
.copyright{left:0;top:1090px;width:1200px;text-align:center;font-size:12.5px;color:#777;padding-right:0}
</style>
</head>
<body>

<header class="abs site-header"></header>
<div class="abs brand"><span>Lantern</span><span class="brand-dot"></span></div>
<a class="abs top-tab tab-signin">SIGN IN</a>
<a class="abs top-tab tab-language">LANGUAGE</a>
<div class="abs nav-panel"></div>
<nav class="abs main-nav">
  <a class="active">HOME</a><a>WHO WE ARE</a><a>CROSS THE LANTERN</a><a>PERFORMANCE SOLUTIONS</a><a>SUSTAIN SOLUTION</a><a>JOIN US</a>
</nav>

<section class="abs hero">
  <div class="hero-photo" role="img" aria-label="Coastal road curving along a sea cliff"></div>
</section>
<h1 class="abs hero-title">LOREM IPSUM DOLOR</h1>
<p class="abs hero-line hero-line-1">LOREM IPSUM <b>DOLOR</b> SIT</p>
<p class="abs hero-line hero-line-2">LOREM <b>IPSUM</b> DOLOR SIT</p>
<a class="abs btn-red hero-signup">SIGNUP NOW
  <svg width="22" height="26" viewBox="0 0 22 26"><path d="M2 2 L20 13 L2 24 Z" fill="#f26a50"/></svg>
</a>
<div class="abs hero-dots"><span class="on"></span><span></span><span></span><span></span></div>

<div class="abs search-band"></div>
<div class="abs search-input">Search...</div>
<div class="abs search-go">GO</div>

<h2 class="abs welcome"><small>WELCOME TO</small> Lantern Performance Group</h2>

<section class="abs intro-slider">
  <svg class="slide-arrow" style="left:10px" width="22" height="22" viewBox="0 0 22 22"><circle cx="11" cy="11" r="10" fill="#222"/><path d="M11 1 A10 10 0 0 0 11 21 Z" fill="#888"/></svg>
  <h3>LOREM IPSUM DOLOR SIT AMET, CONSECTETUR</h3>
  <p class="p1">lLorem ipsum dolor sit amet, consectetur adipiscing elit. Suspendisse mollis mi sed lacus</p>
  <p class="p2">Lorem ipsum dolor sit amet, consectetur adipiscing elit. Suspendisse mollis mi sed lacus elit. Suspendisse mollis mi sed lacus</p>
  <svg class="slide-arrow" style="left:1062px" width="22" height="22" viewBox="0 0 22 22"><circle cx="11" cy="11" r="10" fill="#222"/><path d="M4 18 L18 4" stroke="#ddd" stroke-width="2"/></svg>
</section>

<h3 class="abs col-heading col-1"><span>Lorem ipsum dolor</span></h3>
<h3 class="abs col-heading col-2"><span>News</span></h3>
<h3 class="abs col-heading col-3"><span>Lorem ipsum dol</span></h3>

<div class="abs video-frame">
  <div class="video-still" role="img" aria-label="Intro video still of a business handshake in front of a flag"></div>
  <div class="video-controls">
    <svg width="328" height="36" viewBox="0 0 328 36">
      <circle cx="17" cy="18" r="12" fill="#555" stroke="#aaa" stroke-width="2"/>
      <path d="M13 11 L23 18 L13 25 Z" fill="#111"/>
      <rect x="40" y="14" width="174" height="8" fill="#aaa"/>
      <rect x="40" y="14" width="26" height="8" fill="#fff"/>
      <path d="M233 13 H238 L244 8 V28 L238 23 H233 Z" fill="#777"/>
      <path d="M248 12 Q252 18 248 24 M252 9 Q258 18 252 27" stroke="#777" stroke-width="2" fill="none"/>
      <path d="M290 10 L296 16 M290 10 V14 M290 10 H294 M306 10 L300 16 M306 10 V14 M306 10 H302 M290 26 L296 20 M290 26 V22 M290 26 H294 M306 26 L300 20 M306 26 V22 M306 26 H302" stroke="#777" stroke-width="2" fill="none"/>
    </svg>
  </div>
</div>

<section class="abs news-box">
  <p class="news-item news-1">Lorem ipsum dolor sit amet, consectetur adipiscing elit. Suspendisse mollis mi sed lacus ullamcorper elementum. Vivamus</p>
  <p class="news-item news-2">Lorem ipsum dolor sit amet, consectetur adipiscing elit. Suspendisse mollis mi sed lacus ullamcorper elementum. Vivamus</p>
</section>

<section class="abs promo-box">
  <div class="promo-photo" role="img" aria-label="Smiling business team in front of a flag"></div>
  <p class="promo-title">UP YOUR WIN POWER !</p>
  <a class="btn-red promo-signup">SIGN UP &nbsp;NOW</a>
</section>

<footer class="abs site-footer"></footer>
<nav class="abs footer-nav">
  <a class="active">Home</a><a>Who we are</a><a>Cross the Lantern</a><a>Performance Solutions</a><a>Sustain Solution</a><a>Join Us</a>
</nav>
<p class="abs copyright">© Copyright 2012 advfgtrwrewersfd. All Rights Reserved.</p>

</body>
</html>
```